Asian simmer/ cooking sauce label

We are a established small gourmet condiment company with a range of products. This is a new product range of 6 simmer sauces that we would like a label designed that represents our brand but individualizes the new range.
the label should have a upmarket authentic feel and represent Asian cooking done in a home made kitchen
There will be six varieties it they will al have the same generic design only the product details will change

Our current range can be viewed on our website www.plumwicket.com.au

Butter Chicken has been uploaded. it is one of the products that will be used with the new label
I have uploaded a drinking chocolate label we use that has a black pattern

Target Market(s)

gourmet food shops, gifts stores

Colors

Designer to choose colors to be used in the design.

Requirements
Must have
• the labels needs to include product name. product description, ingredients, weight, nutritional panel, manufactures details and be a sized to suit jars which I will supply
• label size aprox 200mm long x 70mm high
Nice to have
• We prefer warm colours, gold, and black
• our brand name and logo
Should not have
• surprise me

```html
<!DOCTYPE html>
<html lang="en">
<head>
<meta charset="utf-8">
<title>Green Curry Simmer Sauce Label</title>
<link rel="stylesheet" href="https://fonts.googleapis.com/css2?family=Ribeye&family=Josefin+Sans:wght@300;700&family=Oswald:wght@600&display=swap">
<style>
  :root {
    --backdrop: #d8d1a5;
    --label-white: #ffffff;
    --label-black: #0d0d0d;
    --gold: #d9c594;
    --gold-deep: #b9a36d;
    --blossom: #f2b9c4;
    --bowl-green: #9fb27a;
  }
  * { margin: 0; padding: 0; box-sizing: border-box; }
  html, body {
    width: 1200px; height: 894px; overflow: hidden;
    background: var(--backdrop);
  }
  .label {
    position: absolute; left: 330px; top: 110px;
    width: 540px; height: 674px;
    background: var(--label-black);
    box-shadow: 0 6px 24px rgba(0,0,0,.18);
  }
  .label__hero {
    position: absolute; left: 0; top: 0; width: 100%; height: 280px;
    background: var(--label-white);
  }
  .hero__blossom-left {
    position: absolute; left: 0; top: 20px; width: 190px; height: 170px;
    background: radial-gradient(ellipse at 40% 45%, var(--blossom) 0%, rgba(242,185,196,.35) 45%, rgba(255,255,255,0) 72%);
  }
  .hero__blossom-right {
    position: absolute; right: 0; top: 0; width: 120px; height: 110px;
    background: radial-gradient(ellipse at 60% 50%, var(--blossom) 0%, rgba(242,185,196,.3) 45%, rgba(255,255,255,0) 72%);
  }
  .hero__dish {
    position: absolute; left: 120px; top: 40px; width: 330px; height: 230px;
    border-radius: 50%;
    background: radial-gradient(ellipse at 50% 45%, #e9e6d8 0%, var(--bowl-green) 45%, #6f6a55 70%, #f3f3f0 72%, rgba(255,255,255,0) 78%);
  }
  .label__panel {
    position: absolute; left: 0; top: 280px; width: 100%; height: 394px;
  }
  .panel__frame {
    position: absolute; inset: 12px 14px 14px;
    border: 2px solid var(--gold-deep);
  }
  .brand {
    position: absolute; left: 0; right: 0; top: 36px;
    display: flex; align-items: center; justify-content: center; gap: 12px;
    font-family: "Josefin Sans", sans-serif; font-weight: 700;
    font-size: 22px; letter-spacing: 6px; color: var(--gold);
    text-transform: uppercase;
  }
  .brand__mark { width: 16px; height: 16px; background: var(--gold); }
  .product__name {
    position: absolute; left: 40px; right: 40px; top: 124px; text-align: center;
    font-family: "Ribeye", serif; font-size: 50px; letter-spacing: 0;
    font-weight: 400; white-space: nowrap;
    color: var(--gold); line-height: 1;
  }
  .product__type {
    position: absolute; left: 0; right: 0; top: 196px; text-align: center;
    font-family: "Josefin Sans", sans-serif; font-weight: 300;
    font-size: 32px; letter-spacing: 4px; color: var(--gold);
  }
  .product__weight {
    position: absolute; left: 0; right: 0; top: 300px; text-align: center;
    font-family: "Oswald", sans-serif; font-weight: 600;
    font-size: 24px; color: var(--gold);
  }
</style>
</head>
<body>
  <main class="label">
    <section class="label__hero">
      <div class="hero__blossom-left" role="img" aria-label="Cherry blossom branch"></div>
      <div class="hero__blossom-right" role="img" aria-label="Cherry blossom sprig"></div>
      <div class="hero__dish" role="img" aria-label="Photo of a noodle bowl with herbs, lime and chopsticks"></div>
    </section>
    <section class="label__panel">
      <div class="panel__frame"></div>
      <div class="brand"><span class="brand__mark"></span>Corran Treats</div>
      <h1 class="product__name">GREEN CURRY</h1>
      <p class="product__type">SIMMER SAUCE</p>
      <p class="product__weight">NET WT 16OZ (453G)</p>
    </section>
  </main>
</body>
</html>
```